The First Annual Tamsworth Legacy Supper

Something similar to the attached but an attention grabber. It needs to attract people with money to spend!

```html
<!DOCTYPE html>
<html lang="en">
<head>
<meta charset="utf-8">
<title>The First Annual Tamsworth Legacy Supper</title>
<link href="https://fonts.googleapis.com/css2?family=Montserrat:wght@300;400;500;600;700;800&family=Oswald:wght@200;500;700&display=swap" rel="stylesheet">
<style>
:root{
  --navy:#1b3564;
  --sky:#7b9fd6;
  --white:#ffffff;
  --ink:#2d3340;
  --pale:#f3f5f9;
  --stage:#eceef2;
  --shadow:#c7cad0;
}
*{box-sizing:border-box;margin:0;padding:0}
html,body{width:691px;height:1200px;overflow:hidden;background:var(--stage)}
body{font-family:'Montserrat',sans-serif;color:var(--ink)}
.flyer{position:absolute;left:20px;top:178px;width:651px;height:844px;background:var(--white);overflow:hidden;box-shadow:0 6px 18px rgba(0,0,0,.18)}
.abs{position:absolute}
.shapes{position:absolute;left:0;top:0}
.ticket-column{position:absolute;left:345px;top:295px;width:306px;height:458px;background:var(--pale)}

.hero-photo{position:absolute;left:344px;top:0;width:307px;height:295px;
  clip-path:polygon(94px 0,100% 0,100% 100%,0 100%);
  background:linear-gradient(180deg,#2f4d7e 0%,#6f86aa 35%,#54606f 62%,#2c3644 80%,#5d7290 100%)}

.presents{left:35px;top:33px;font-size:12px;font-weight:500;color:var(--white);letter-spacing:.3px}
.title{left:35px;top:60px;font-family:'Oswald',sans-serif;color:var(--white);font-size:40px;line-height:42px;letter-spacing:-.3px;text-transform:uppercase}
.title .thin{font-weight:200;display:block}
.title .bold{font-weight:700;display:block}
.date{left:35px;top:229px;font-size:16px;line-height:21px;color:var(--white);text-transform:uppercase}
.date b{font-weight:700}

.auction-heading{left:34px;top:318px;font-size:18px;line-height:21px;color:var(--navy);text-transform:uppercase;font-weight:400}
.auction-heading b{font-weight:800}
.intro{left:34px;top:388px;width:295px;font-size:9.3px;line-height:11.5px;color:#3a3f4a}
.intro p{margin-bottom:11px}
.rule{position:absolute;border-top:1px dashed var(--sky)}
.gallery-photo{position:absolute;top:544px;height:151px;border:1px solid var(--sky)}
.gallery-photo.patio{left:34px;width:140px;background:linear-gradient(180deg,#4f6b3a 0%,#3d5230 35%,#8a5a3c 55%,#d9d6d0 75%,#9fa6ad 100%)}
.gallery-photo.bedroom{left:185px;width:141px;background:linear-gradient(135deg,#e9ecef 0%,#c9d6e2 35%,#e7b37a 60%,#f0ede8 100%)}

.follow{left:59px;top:722px;font-size:9.5px;line-height:11.5px;color:var(--navy)}
.follow b{font-weight:700;text-transform:uppercase;letter-spacing:.2px}
.follow span{font-weight:600;display:block}

.host-photo{position:absolute;top:767px;width:53px;height:56px;border:2px solid var(--white);background:linear-gradient(180deg,#e7e9ec 0%,#c5c9cf 55%,#3b4150 100%)}
.host{color:var(--white);top:769px}
.host .name{font-size:9px;font-weight:500;text-transform:uppercase;letter-spacing:.3px}
.host .phone{font-size:12px;font-weight:700;display:flex;align-items:center;gap:3px;margin-top:1px}
.contact{left:318px;top:810px;width:232px;display:flex;align-items:center;gap:10px;color:var(--white)}
.contact .cta{font-size:15px;font-weight:400;letter-spacing:.5px}
.contact .cta b{font-weight:800}
.contact .divider{width:1px;height:20px;background:var(--white)}
.contact .alt{font-size:9.5px;line-height:9.5px;text-transform:uppercase}
.contact .alt b{font-weight:800;display:block}

.right-text{left:370px}
.tickets-heading{font-size:18px;line-height:17.5px;color:var(--navy);text-transform:uppercase;font-weight:400;letter-spacing:.3px}
.tickets-heading b{font-weight:800;display:block}
.price-band{position:absolute;left:365px;width:286px;height:35px;background:var(--sky);border-top:1px dashed var(--navy);border-bottom:1px dashed var(--navy);font-family:'Oswald',sans-serif;font-weight:500;font-size:24px;line-height:33px;color:var(--white);padding-left:14px;text-transform:uppercase;letter-spacing:-.2px}
.couple{top:404px;font-size:18px;color:var(--navy);text-transform:uppercase;letter-spacing:.5px}
.couple b{font-weight:800}
.double-rule{position:absolute;left:365px;top:440px;width:286px;height:4px;border-top:1px solid #6b7280;border-bottom:1px solid #6b7280}
.donated{top:561px;font-size:13px;line-height:17px;color:var(--navy)}
.donated b{font-weight:800;text-transform:uppercase}
.donated .donor{display:block;letter-spacing:.6px;font-weight:500}
.donated .donor i{font-style:normal;font-weight:400}
.value-band{position:absolute;left:365px;top:602px;width:286px;height:35px;border-top:1px dashed var(--navy);border-bottom:1px dashed var(--navy);display:flex;align-items:center;padding-left:5px}
.value-band .label{font-size:22px;font-weight:300;color:#1d2330;letter-spacing:.5px;width:93px}
.value-band .amount{background:var(--navy);color:var(--white);font-weight:800;font-size:20px;height:29px;line-height:29px;padding:0 9px}
.value-band .fill{flex:1;height:100%;background:var(--sky)}
.outlets-heading{top:645px;font-size:11.5px;color:var(--navy);text-transform:uppercase}
.outlets-heading b{font-weight:800}
.outlet{display:flex;gap:6px;align-items:flex-start}
.outlet .name{font-size:11.5px;color:var(--navy);text-transform:uppercase;margin-bottom:2px;white-space:nowrap}
.outlet .name b{font-weight:800}
.outlet .addr{font-size:8.6px;line-height:9.5px;font-weight:700;color:#2d3340}
.store .name{font-size:10.5px}
.store .addr{font-size:8px;line-height:9px}
.pin{flex:none;width:14px;height:14px}
</style>
</head>
<body>
<main class="flyer">
  <svg class="shapes" width="651" height="844" viewBox="0 0 651 844" aria-hidden="true">
    <rect x="0" y="0" width="651" height="217" fill="var(--navy)"/>
    <rect x="0" y="217" width="440" height="78" fill="var(--sky)"/>
  </svg>

  <div class="ticket-column"></div>
  <div class="hero-photo" role="img" aria-label="Photo of a modern two-storey house at dusk with lit windows and a wet reflective driveway"></div>

  <svg class="shapes" width="651" height="844" viewBox="0 0 651 844" aria-hidden="true">
    <rect x="0" y="722" width="48" height="20" fill="var(--navy)"/>
    <circle cx="26" cy="732" r="6" fill="none" stroke="var(--white)" stroke-width="1.3"/>
    <rect x="566" y="748" width="85" height="96" fill="var(--shadow)"/>
    <polygon points="0,753 370,753 549,844 0,844" fill="var(--navy)"/>
    <rect x="0" y="829" width="60" height="6" fill="var(--sky)"/>
    <polygon points="322,805 548,805 548,838 310,838" fill="var(--sky)"/>
  </svg>

  <p class="abs presents">THE TAMSWORTH COMMUNITY HALL PRESENTS</p>
  <h1 class="abs title"><span class="thin">The First Annual</span><span class="bold">Tamsworth Legacy</span><span class="bold">Supper</span></h1>
  <p class="abs date"><b>April 23, 2022</b> starting at<br><b>5:00 PM</b> with cocktail hour</p>

  <h2 class="abs auction-heading"><b>Live auction,</b> silent<br>auction, raffle and<br><b>a cash bar!</b></h2>
  <div class="abs intro">
    <p>Come on out to the Tamsworth Community Hall for a delicious prime rib dinner, drinks, entertainment and more! There will be plenty of amazing auction items for everyone to choose from.</p>
    <p>All proceeds will go to the Tamsworth Community Hall. We will share some history of the school and each year we will highlight a local family. This year will be the Harlow family who have been here for ....years!!</p>
    <p>High Side Barn, dirt bike, custom knives, a pack trip and so much more!</p>
  </div>
  <div class="rule" style="left:34px;top:535px;width:294px"></div>
  <div class="gallery-photo patio" role="img" aria-label="Photo of a covered backyard patio with garden and outdoor seating"></div>
  <div class="gallery-photo bedroom" role="img" aria-label="Photo of a bright bedroom with glass doors opening to a terrace"></div>
  <div class="rule" style="left:34px;top:707px;width:294px"></div>
  <p class="abs follow"><b>Follow the Tamsworth Community Hall's</b><span>social page to see all the auction items available!</span></p>

  <div class="host-photo" style="left:34px" role="img" aria-label="Portrait photo of host Marla Keene"></div>
  <div class="abs host" style="left:97px">
    <p class="name">Marla Keene</p>
    <p class="phone"><svg width="10" height="10" viewBox="0 0 24 24" aria-hidden="true"><path fill="#fff" d="M6.6 10.8a15.1 15.1 0 0 0 6.6 6.6l2.2-2.2a1 1 0 0 1 1-.25 11.4 11.4 0 0 0 3.6.57 1 1 0 0 1 1 1V20a1 1 0 0 1-1 1A17 17 0 0 1 3 4a1 1 0 0 1 1-1h3.5a1 1 0 0 1 1 1c0 1.25.2 2.45.57 3.57a1 1 0 0 1-.25 1z"/></svg>(555)214-0381</p>
  </div>
  <div class="host-photo" style="left:213px" role="img" aria-label="Portrait photo of host Dana Holt"></div>
  <div class="abs host" style="left:277px">
    <p class="name">Dana Holt</p>
    <p class="phone"><svg width="10" height="10" viewBox="0 0 24 24" aria-hidden="true"><path fill="#fff" d="M6.6 10.8a15.1 15.1 0 0 0 6.6 6.6l2.2-2.2a1 1 0 0 1 1-.25 11.4 11.4 0 0 0 3.6.57 1 1 0 0 1 1 1V20a1 1 0 0 1-1 1A17 17 0 0 1 3 4a1 1 0 0 1 1-1h3.5a1 1 0 0 1 1 1c0 1.25.2 2.45.57 3.57a1 1 0 0 1-.25 1z"/></svg>(555)376-2049</p>
  </div>
  <div class="abs contact">
    <span class="cta">CONTACT <b>US</b></span>
    <span class="divider"></span>
    <span class="alt">Or get<b>them from</b></span>
  </div>

  <h2 class="abs tickets-heading right-text" style="top:316px"><b>Tickets for the</b>event are</h2>
  <div class="price-band" style="top:362px">$50 each or $90</div>
  <p class="abs couple right-text">For a <b>couple</b></p>
  <div class="double-rule"></div>
  <h2 class="abs tickets-heading right-text" style="top:463px"><b>Tickets for the</b>10x12 high side barn</h2>
  <div class="price-band" style="top:513px">$25 each or 5 for $100</div>
  <p class="abs donated right-text"><b>Donated</b> BY:<span class="donor">Ridgeline Shed Co. <i>of Larkfield</i></span></p>
  <div class="value-band"><span class="label">VALUE</span><span class="amount">$6500</span><span class="fill"></span></div>
  <p class="abs outlets-heading right-text"><b>Get your</b> tickets from:</p>
  <div class="abs outlet right-text" style="top:665px">
    <svg class="pin" viewBox="0 0 24 24" aria-hidden="true"><circle cx="12" cy="12" r="10.5" fill="none" stroke="var(--navy)" stroke-width="1.5"/><path fill="var(--navy)" d="M12 5.5a4.2 4.2 0 0 0-4.2 4.2c0 3.1 4.2 7.8 4.2 7.8s4.2-4.7 4.2-7.8A4.2 4.2 0 0 0 12 5.5zm0 5.8a1.6 1.6 0 1 1 0-3.2 1.6 1.6 0 0 1 0 3.2z"/></svg>
    <p class="addr">Ridgeline Shed Co. in Larkfield<br>42 Orchard Ln, Larkfield</p>
  </div>
  <div class="rule" style="left:370px;top:694px;width:255px;border-color:#9aa3b2"></div>
  <div class="abs right-text" style="top:703px">
    <p class="outlet"><span class="name"><b>Summit Peak</b> Realty</span></p>
    <div class="outlet">
      <svg class="pin" viewBox="0 0 24 24" aria-hidden="true"><circle cx="12" cy="12" r="10.5" fill="none" stroke="var(--navy)" stroke-width="1.5"/><path fill="var(--navy)" d="M12 5.5a4.2 4.2 0 0 0-4.2 4.2c0 3.1 4.2 7.8 4.2 7.8s4.2-4.7 4.2-7.8A4.2 4.2 0 0 0 12 5.5zm0 5.8a1.6 1.6 0 1 1 0-3.2 1.6 1.6 0 0 1 0 3.2z"/></svg>
      <p class="addr" style="margin-top:2px">218 W Maple St, Larkfield</p>
    </div>
  </div>
  <div class="rule" style="left:370px;top:743px;width:180px;border-color:#9aa3b2"></div>
  <div class="abs store" style="left:440px;top:750px;width:116px">
    <p class="outlet"><span class="name"><b>Tamsworth</b> Store</span></p>
    <div class="outlet">
      <svg class="pin" viewBox="0 0 24 24" aria-hidden="true"><circle cx="12" cy="12" r="10.5" fill="none" stroke="var(--navy)" stroke-width="1.5"/><path fill="var(--navy)" d="M12 5.5a4.2 4.2 0 0 0-4.2 4.2c0 3.1 4.2 7.8 4.2 7.8s4.2-4.7 4.2-7.8A4.2 4.2 0 0 0 12 5.5zm0 5.8a1.6 1.6 0 1 1 0-3.2 1.6 1.6 0 0 1 0 3.2z"/></svg>
      <p class="addr">4120 County Road 9,<br>Tamsworth</p>
    </div>
  </div>
  <div class="abs" style="left:560px;top:738px;width:78px;height:90px;border:2px solid var(--white);background:linear-gradient(180deg,#b8c4cf 0%,#6e7a86 40%,#3e3a36 70%,#8c8f92 100%)" role="img" aria-label="Photo of a covered porch with outdoor chairs and glass doors"></div>
</main>
</body>
</html>
```